Sign Design

We already have a logo, but would like to design 2 x signs.
Sign 1:
Dimensions 1500mm wide x 2500m high.
Information to include on sign: - Clinic name and logo (attached)
- the word "DENTIST "
- Street number (which is 348)
Phone number (which is 6153 4097)

Sign 2:
Dimensions: 800mm wide x 600mm high

```html
<!DOCTYPE html>
<html lang="en">
<head>
<meta charset="utf-8">
<title>Brookvale Dental Care – Signage</title>
<link rel="stylesheet" href="https://fonts.googleapis.com/css2?family=Poppins:wght@700;800&family=Arimo:wght@400&display=swap">
<style>
  :root {
    --lime: #a2dd4a;
    --forest: #136f39;
    --leaf: #15b21f;
    --white: #ffffff;
    --edge: #a2dd4a;
    --ink: #222222;
  }
  html, body {
    margin: 0;
    padding: 0;
    width: 1200px;
    height: 1200px;
    overflow: hidden;
    background: var(--white);
  }
  .canvas {
    position: relative;
    width: 1200px;
    height: 1200px;
  }
  svg { position: absolute; left: 0; top: 0; }
  .street-number { font-family: "Poppins", sans-serif; font-weight: 700; fill: var(--lime); }
  .phone { font-family: "Poppins", sans-serif; font-weight: 800; fill: var(--forest); }
  .sign-word { font-family: "Poppins", sans-serif; font-weight: 800; fill: var(--white); }
  .clinic-name { font-family: "Arimo", sans-serif; font-weight: 400; fill: var(--forest); }
</style>
</head>
<body>
<div class="canvas">
  <svg width="1200" height="1200" viewBox="0 0 1200 1200" xmlns="http://www.w3.org/2000/svg">
    <defs>
      <clipPath id="tall-sign-clip">
        <rect x="71" y="115" width="574" height="957"/>
      </clipPath>
    </defs>

    <!-- Tall pylon sign -->
    <g class="tall-sign" clip-path="url(#tall-sign-clip)">
      <rect class="tall-sign__panel" x="71" y="115" width="574" height="680" fill="var(--lime)"/>
      <rect class="tall-sign__base" x="71.5" y="795" width="573" height="276.5" fill="var(--white)" stroke="var(--edge)" stroke-width="1"/>

      <rect class="number-box" x="113" y="116" width="174" height="220" fill="var(--forest)"/>
      <text class="street-number" x="200" y="292" font-size="98" text-anchor="middle" textLength="142" lengthAdjust="spacingAndGlyphs">348</text>
      <text class="phone" x="200" y="391" font-size="31" text-anchor="middle" textLength="170" lengthAdjust="spacingAndGlyphs">6153 4097</text>

      <text class="sign-word" transform="translate(645 800) rotate(-90)" x="0" y="0" font-size="178" textLength="690" lengthAdjust="spacingAndGlyphs">DENTIST</text>

      <g class="clinic-lockup">
        <circle cx="182" cy="935" r="38" fill="var(--forest)"/>
        <text class="clinic-name" x="286" y="934" font-size="60">Brookvale</text>
        <text class="clinic-name" x="390" y="978" font-size="34">Dental Care</text>
      </g>
    </g>

    <!-- Small panel sign -->
    <g class="panel-sign">
      <rect x="765" y="514" width="306" height="230" fill="var(--lime)"/>
      <path d="M765,588 C860,570 1030,575 1071,652 L1071,744 L765,744 Z" fill="var(--white)"/>
      <path d="M765,598 C860,582 1030,587 1071,662" fill="none" stroke="var(--forest)" stroke-width="4"/>
      <rect x="765" y="514" width="306" height="230" fill="none" stroke="var(--ink)" stroke-width="0.7"/>

      <g class="clinic-lockup">
        <circle cx="815" cy="680" r="22" fill="var(--forest)"/>
        <text class="clinic-name" x="876" y="680" font-size="32">Brookvale</text>
        <text class="clinic-name" x="936" y="705" font-size="18">Dental Care</text>
      </g>
    </g>
  </svg>
</div>
</body>
</html>
```